Modern Business Card

Modern professional business card with more than just logo and demographic info. Something memorable.

We are a trendy/modern chiropractic group with an emphasis on neurology, hence the minimalist-type brain logo. We want to convey that modern and technical aspect with professionalism and the elite nature of our practice environment.

```html
<!DOCTYPE html>
<html lang="en">
<head>
<meta charset="utf-8">
<title>Kinetra Spine Care – Business Card</title>
<link rel="stylesheet" href="https://fonts.googleapis.com/css2?family=Open+Sans:wght@400;600;700&display=swap">
<style>
  :root {
    --canvas: #ffffff;
    --card: #ffffff;
    --brand-blue: #4a7fc1;
    --ink: #111111;
    --muted: #5f5f5f;
    --shadow: rgba(0, 0, 0, 0.12);
  }
  * { margin: 0; padding: 0; box-sizing: border-box; }
  html, body {
    width: 1200px;
    height: 1200px;
    overflow: hidden;
    background: var(--canvas);
    font-family: "Open Sans", Arial, sans-serif;
  }
  .canvas {
    position: relative;
    width: 1200px;
    height: 1200px;
  }
  .card {
    position: absolute;
    left: 115px;
    width: 970px;
    height: 553px;
    background: var(--card);
    box-shadow: 0 2px 14px var(--shadow);
  }
  .card--front { top: 42px; }
  .card--back { top: 605px; }

  /* Front brand lockup */
  .brand-front {
    position: absolute;
    left: 0;
    right: 0;
    top: 160px;
    display: flex;
    flex-direction: column;
    align-items: center;
  }
  .brand-dot {
    width: 104px;
    height: 104px;
    border-radius: 50%;
    background: var(--brand-blue);
  }
  .brand-name {
    color: var(--ink);
    font-weight: 600;
    text-transform: uppercase;
    letter-spacing: 2px;
    line-height: 1.1;
  }
  .brand-front .brand-name {
    margin-top: 32px;
    font-size: 40px;
    text-align: center;
  }

  /* Back brand lockup */
  .brand-back {
    position: absolute;
    left: 70px;
    top: 70px;
    display: flex;
    align-items: center;
    gap: 22px;
  }
  .brand-back .brand-dot {
    width: 104px;
    height: 104px;
  }
  .brand-back .brand-name {
    font-size: 36px;
  }

  .person {
    position: absolute;
    right: 74px;
    top: 84px;
    text-align: right;
  }
  .person__name {
    font-size: 35px;
    font-weight: 700;
    color: var(--ink);
    line-height: 1.2;
  }
  .person__title {
    font-size: 26px;
    color: var(--muted);
    margin-top: 2px;
  }

  .address {
    position: absolute;
    left: 70px;
    top: 377px;
    font-size: 26px;
    line-height: 35px;
    color: var(--muted);
    font-style: normal;
  }

  .contact {
    position: absolute;
    left: 573px;
    top: 374px;
    list-style: none;
    font-size: 27px;
    line-height: 36px;
    color: var(--muted);
  }
  .contact li {
    display: flex;
    align-items: center;
    gap: 14px;
  }
  .contact svg {
    width: 24px;
    height: 24px;
    fill: var(--brand-blue);
    flex: none;
  }
</style>
</head>
<body>
<main class="canvas">
  <section class="card card--front" aria-label="Card front">
    <div class="brand-front">
      <span class="brand-dot" aria-hidden="true"></span>
      <p class="brand-name">Kinetra<br>Spine Care</p>
    </div>
  </section>

  <section class="card card--back" aria-label="Card back">
    <div class="brand-back">
      <span class="brand-dot" aria-hidden="true"></span>
      <p class="brand-name">Kinetra<br>Spine Care</p>
    </div>

    <div class="person">
      <p class="person__name">Daniel Reyes</p>
      <p class="person__title">President</p>
    </div>

    <address class="address">
      Street Name Here<br>
      Suite 100 Street Zip Code<br>
      Country
    </address>

    <ul class="contact">
      <li>
        <svg viewBox="0 0 24 24" aria-hidden="true"><path d="M6.6 10.8c1.4 2.8 3.8 5.1 6.6 6.6l2.2-2.2c.3-.3.7-.4 1-.2 1.1.4 2.3.6 3.6.6.6 0 1 .4 1 1V20c0 .6-.4 1-1 1C10.6 21 3 13.4 3 4c0-.6.4-1 1-1h3.5c.6 0 1 .4 1 1 0 1.3.2 2.5.6 3.6.1.3 0 .7-.2 1l-2.3 2.2z"/></svg>
        <span>01234-56789</span>
      </li>
      <li>
        <svg viewBox="0 0 24 24" aria-hidden="true"><path d="M2 5h20v14H2V5zm2 2v.3l8 5.2 8-5.2V7H4zm0 2.7V17h16V9.7l-8 5.2-8-5.2z"/></svg>
        <span>info@yourwebsite.com</span>
      </li>
      <li>
        <svg viewBox="0 0 24 24" aria-hidden="true"><path d="M12 2a10 10 0 1 0 0 20 10 10 0 0 0 0-20zm6.9 6h-2.9a15 15 0 0 0-1.4-3.6A8 8 0 0 1 18.9 8zM12 4c.8 1.2 1.5 2.5 1.9 4h-3.8c.4-1.5 1.1-2.8 1.9-4zM4.3 14a8 8 0 0 1 0-4h3.4a16 16 0 0 0 0 4H4.3zm.8 2h2.9c.3 1.3.8 2.5 1.4 3.6A8 8 0 0 1 5.1 16zM8 8H5.1a8 8 0 0 1 4.3-3.6C8.8 5.5 8.3 6.7 8 8zm4 12c-.8-1.2-1.5-2.5-1.9-4h3.8c-.4 1.5-1.1 2.8-1.9 4zm2.3-6H9.7a14 14 0 0 1 0-4h4.6a14 14 0 0 1 0 4zm.3 5.6c.6-1.1 1.1-2.3 1.4-3.6h2.9a8 8 0 0 1-4.3 3.6zM16.3 14a16 16 0 0 0 0-4h3.4a8 8 0 0 1 0 4h-3.4z"/></svg>
        <span>www.yourwebsite.com</span>
      </li>
    </ul>
  </section>
</main>
</body>
</html>
```